Letterhead Design for Higher Education provider

Company Name: PVRA Credentials
Motto: Quality in Learning
Address: Kelmont House, Harrier Lane, Fernbrook Trade Park, Dartford DA4 2RX, United Kingdom
T: +44 (0)20 7946 0582
E: info@pvra-example.org.uk
W: www.pvra-example.org.uk
Legal information: PVRA Credentials is incorporated in England & Wales | Company Reg. No. 07315428

Target Market(s)

Higher Education provider

Industry/Entity Type

Education

Font styles to use
Sans Serif

Requirements
Must have
• Company Name, Address, tel, email, web, company legal information.
Nice to have
• motto
Should not have
• should not cover to much of printing areas

```html
<!DOCTYPE html>
<html lang="en">
<head>
<meta charset="utf-8">
<title>PVRA Credentials Letterhead</title>
<link href="https://fonts.googleapis.com/css2?family=Lato:wght@400;700&display=swap" rel="stylesheet">
<style>
  :root {
    --backdrop: #d9d9d9;
    --paper: #ffffff;
    --brand-blue: #1f3f8f;
    --text-grey: #8a8a8a;
    --rule-grey: #9a9a9a;
  }
  * { margin: 0; padding: 0; box-sizing: border-box; }
  html, body {
    width: 1200px;
    height: 1000px;
    overflow: hidden;
    background: var(--backdrop);
    font-family: "Lato", Arial, sans-serif;
  }
  .letterhead {
    position: absolute;
    left: 269px;
    top: 34px;
    width: 662px;
    height: 932px;
    background: var(--paper);
    box-shadow: 0 2px 8px rgba(0,0,0,0.12);
  }
  .brand {
    position: absolute;
    left: 44px;
    top: 46px;
  }
  .brand-name {
    font-size: 18px;
    font-weight: 700;
    color: var(--brand-blue);
    line-height: 1;
  }
  .footer {
    position: absolute;
    left: 44px;
    right: 44px;
    bottom: 48px;
  }
  .footer-rule {
    border-top: 1px solid var(--rule-grey);
    margin-bottom: 14px;
  }
  .footer-columns {
    display: flex;
    justify-content: space-between;
    font-size: 9.5px;
    line-height: 1.45;
    color: var(--text-grey);
  }
  .company-title {
    color: var(--brand-blue);
    font-weight: 700;
    font-size: 11px;
  }
  .motto {
    font-size: 10.5px;
    margin-bottom: 6px;
  }
  .legal-name {
    color: var(--text-grey);
    font-weight: 700;
  }
</style>
</head>
<body>
  <main class="letterhead">
    <header class="brand">
      <span class="brand-name">PVRA Credentials</span>
    </header>

    <footer class="footer">
      <div class="footer-rule"></div>
      <div class="footer-columns">
        <div class="footer-address">
          <div class="company-title">PVRA Credentials</div>
          <div class="motto">Quality in Learning</div>
          <div>A: Kelmont House, Harrier Lane,</div>
          <div>Fernbrook Trade Park,</div>
          <div>Dartford DA4 2RX, United Kingdom</div>
        </div>
        <div class="footer-contact">
          <div>T: +44 (0)20 7946 0582</div>
          <div>E: info@pvra-example.org.uk</div>
          <div>W: www.pvra-example.org.uk</div>
        </div>
        <div class="footer-legal">
          <div class="legal-name">PVRA Credentials</div>
          <div>is incorporated in England &amp; Wales</div>
          <div>Company Reg. No. 07315428</div>
        </div>
      </div>
    </footer>
  </main>
</body>
</html>
```